Redesign cement bags for leading cement producer in south east asia

We are from Larkfield cement and would like to redesign our bag to relaunch the product line. Our bags are made of high quality PP woven sack. We are one of the leading cement producers and we want our bags to have a Larkfield classy look on each visible side when it is loading in a truck or stacking on a pallet.

Thank you for interesting in this project. Good luck.

Project Deadline Extended Reason: Hi all, I have received requests to extend the deadline. Some of the work requires revising and some of them are still on process. To be fair, I also raise my budget to compensate the time. Thanks all for your participation. Added Sunday, July 10, 2016

Target Market(s)

Construction

Industry/Entity Type

Cement

Requirements
Must have
• You will have to design two bags for two cement grades. 52.5 is of higher grade and 42.5 is of lower grade. Both are similar in design but a distinctive colours to differentiate the two at once. Please look at Reference picture 2 for ideas.
Nice to have
• You do not have to change the original logo but the Larkfield cement word font changes are required. There are no restrictions to colours and font but please refrain from using feminine colours. Instructions on rear side of the bags are now included in the scope. Please create new layout and design new user friendly symbols.
Should not have
• Since cement is a dusty product, you need avoid some colours like black as background. The dust need to be less obvious to attract attention. Our previous base colour are shown in below.
• We want a fresh look on our bag, please do not just copy our old design and make small changes. I have attached our competitors' design, please refrain from using their design as well.
• It is recommend to do some research on cement bag sector.

```html
<!DOCTYPE html>
<html lang="en">
<head>
<meta charset="utf-8">
<title>Larkfield Cement – 52.5 Bag Layout</title>
<link rel="stylesheet" href="https://fonts.googleapis.com/css2?family=Alfa+Slab+One&family=Roboto+Condensed:wght@400;700&family=Roboto:wght@300;400;700&display=swap">
<style>
  :root{
    --red:#d62027;
    --cream:#fdd98f;
    --gold:#fbd889;
    --blue:#0b5aa5;
    --ink:#222;
    --paper:#ffffff;
  }
  *{margin:0;padding:0;box-sizing:border-box}
  html,body{width:1200px;height:858px;overflow:hidden;background:var(--paper)}
  body{font-family:"Roboto",Arial,sans-serif;position:relative}
  .artwork{position:absolute;inset:0;width:1200px;height:858px}
  .t{position:absolute;white-space:nowrap;line-height:1}
  .center{transform:translateX(-50%);text-align:center}

  /* dimension marks */
  .dim{font:700 17px "Roboto",Arial,sans-serif;color:var(--ink);background:var(--paper);padding:0 3px}
  .dim-v{transform:translate(-50%,-50%) rotate(90deg)}

  /* front panel */
  .flap-label{font:700 19px "Roboto",Arial,sans-serif;color:var(--gold);transform:translateX(-50%) rotate(180deg)}
  .flap-label b{font-style:italic;font-size:27px;margin:0 6px}
  .brand-front{font:400 46px "Alfa Slab One",Georgia,serif;color:var(--gold);letter-spacing:1px}
  .brand-seal{font:400 26px "Alfa Slab One",Georgia,serif;color:var(--blue)}
  .front-cement{font:700 40px "Roboto Condensed",Arial,sans-serif;color:var(--red);letter-spacing:1px}
  .spec-title{font:700 18px "Roboto",Arial,sans-serif;color:var(--blue)}
  .spec-std{font:700 15px "Roboto",Arial,sans-serif;color:var(--blue)}
  .export-line{font:300 21px "Roboto",Arial,sans-serif;color:var(--blue)}
  .net-weight{font:400 15px "Roboto",Arial,sans-serif;color:var(--blue)}

  /* gussets */
  .gusset-title{font:400 31px "Alfa Slab One",Georgia,serif;color:var(--gold);transform:translate(-50%,-50%) rotate(-90deg)}
  .gusset-title span{font:700 28px "Roboto Condensed",Arial,sans-serif;margin-left:10px}
  .gusset-seal{font:400 13px "Alfa Slab One",Georgia,serif;color:var(--blue);transform:translate(-50%,-50%)}

  /* back panel */
  .brand-back{font:400 30px "Alfa Slab One",Georgia,serif;color:var(--gold)}
  .brand-back span{font:700 27px "Roboto Condensed",Arial,sans-serif;margin-left:8px}
  .info-bar{position:absolute;left:617px;width:301px;height:14px;background:var(--blue);color:var(--cream);font:700 14px "Roboto Condensed",Arial,sans-serif;text-align:center;line-height:14px}
  .info-text{font:700 8.5px "Roboto",Arial,sans-serif;color:var(--blue)}
  .info-small{font:700 6.6px "Roboto",Arial,sans-serif;color:var(--blue)}
  .mix-head{font:700 8.5px "Roboto",Arial,sans-serif;color:var(--blue)}
  .maker-intro{font:700 11px "Roboto",Arial,sans-serif;color:var(--blue)}
  .maker-name{font:700 17px "Roboto Condensed",Arial,sans-serif;color:var(--blue)}
  .maker-address{font:700 9.6px "Roboto",Arial,sans-serif;color:var(--blue);line-height:12.8px}
  .maker-address .indent{padding-left:26px}
  .grade-label{font:700 19px "Roboto",Arial,sans-serif;color:var(--red)}
  .grade-label b{font-style:italic;font-size:27px;margin:0 8px}
</style>
</head>
<body>
<main class="artwork" aria-label="Larkfield 52.5 cement bag layout">

<svg class="shapes" width="1200" height="858" viewBox="0 0 1200 858" aria-hidden="true" style="position:absolute;inset:0">
  <!-- dimension lines -->
  <g stroke="var(--ink)" stroke-width="1" fill="none">
    <path d="M96 28V48M480 28V48M576 28V48M960 28V48M1056 28V48"/>
    <path d="M96 38H480M480 38H576M576 38H960M960 38H1056"/>
    <path d="M1064 58H1096M1064 154H1096M1064 730H1096M1064 826H1096"/>
    <path d="M1086 58V154M1086 154V730M1086 730V826"/>
  </g>

  <!-- front panel -->
  <rect x="96" y="58" width="384" height="768" fill="var(--cream)"/>
  <rect x="129" y="75" width="316" height="59" fill="var(--red)"/>
  <polygon points="96,154 480,154 480,336 282,452 96,344" fill="var(--red)"/>
  <rect x="96" y="730" width="384" height="96" fill="var(--red)"/>
  <rect x="96" y="664" width="78" height="26" fill="var(--blue)"/>
  <rect x="394" y="664" width="86" height="26" fill="var(--blue)"/>
  <circle cx="282" cy="320" r="84" fill="var(--cream)"/>

  <!-- left gusset -->
  <g class="gusset">
    <rect x="480" y="58" width="96" height="768" fill="var(--red)"/>
    <polygon points="480,152 528,124 576,152 576,336 528,308 480,336" fill="var(--cream)"/>
    <polygon points="480,748 528,720 576,748 576,826 528,800 480,826" fill="var(--cream)"/>
    <circle cx="526" cy="230" r="40" fill="var(--cream)" stroke="var(--red)" stroke-width="2"/>
  </g>

  <!-- back panel -->
  <rect x="576" y="58" width="384" height="768" fill="var(--cream)"/>
  <rect x="576" y="154" width="384" height="198" fill="var(--red)"/>
  <rect x="576" y="730" width="384" height="96" fill="var(--red)"/>
  <rect x="608" y="744" width="320" height="66" fill="var(--cream)"/>
  <circle cx="619" cy="188" r="14" fill="var(--gold)"/>
  <rect x="608" y="221" width="318" height="349" fill="var(--cream)"/>
  <rect x="616.5" y="227.5" width="302" height="341" fill="none" stroke="var(--blue)" stroke-width="1.6"/>

  <!-- mixing measures -->
  <defs>
    <symbol id="measure" viewBox="0 0 10 10">
      <path d="M2 3 L3 9 H7 L8 3 Z M2 3 Q5 0 8 3" fill="none" stroke="var(--blue)" stroke-width="0.9"/>
    </symbol>
  </defs>
  <g class="mix-lean">
    <use href="#measure" x="739" y="320" width="9" height="9"/>
    <use href="#measure" x="775" y="311" width="9" height="9"/>
    <use href="#measure" x="770" y="321" width="9" height="9"/>
    <use href="#measure" x="781" y="321" width="9" height="9"/>
    <use href="#measure" x="823" y="306" width="9" height="9"/>
    <use href="#measure" x="818" y="316" width="9" height="9"/>
    <use href="#measure" x="829" y="316" width="9" height="9"/>
    <use href="#measure" x="818" y="326" width="9" height="9"/>
    <use href="#measure" x="829" y="326" width="9" height="9"/>
    <use href="#measure" x="870" y="320" width="9" height="9"/>
  </g>
  <g class="mix-general">
    <use href="#measure" x="739" y="349" width="9" height="9"/>
    <use href="#measure" x="770" y="349" width="9" height="9"/>
    <use href="#measure" x="781" y="349" width="9" height="9"/>
    <use href="#measure" x="818" y="345" width="9" height="9"/>
    <use href="#measure" x="829" y="345" width="9" height="9"/>
    <use href="#measure" x="818" y="355" width="9" height="9"/>
    <use href="#measure" x="829" y="355" width="9" height="9"/>
    <path d="M871 351 L873 358 H875 V351 Z" fill="none" stroke="var(--blue)" stroke-width="0.8"/>
    <use href="#measure" x="888" y="349" width="9" height="9"/>
  </g>

  <!-- precaution icons -->
  <g fill="var(--blue)">
    <circle cx="643" cy="454" r="8"/>
    <circle cx="643" cy="478" r="8"/>
    <circle cx="643" cy="502" r="8"/>
    <circle cx="643" cy="525" r="8"/>
    <circle cx="643" cy="550" r="8"/>
  </g>
  <g stroke="var(--cream)" stroke-width="1.4" fill="none" stroke-linecap="round">
    <path d="M639 457 L643 451 L647 457"/>
    <path d="M640 482 V475 M643 482 V474 M646 482 V476"/>
    <path d="M638 501 H648 M639 504 H647"/>
    <circle cx="643" cy="523" r="2.5"/><path d="M639 530 Q643 526 647 530"/>
    <path d="M637 550 Q643 543 649 550 M643 550 V555"/>
  </g>

  <!-- manufacturer mark -->
  <circle cx="637" cy="597" r="18" fill="var(--blue)"/>

  <!-- right gusset -->
  <g class="gusset">
    <rect x="960" y="58" width="96" height="768" fill="var(--red)"/>
    <polygon points="960,152 1008,124 1056,152 1056,336 1008,308 960,336" fill="var(--cream)"/>
    <polygon points="960,748 1008,720 1056,748 1056,826 1008,800 960,826" fill="var(--cream)"/>
    <circle cx="1007" cy="230" r="40" fill="var(--cream)" stroke="var(--red)" stroke-width="2"/>
  </g>
</svg>

<!-- dimension labels -->
<div class="t dim center" style="left:285px;top:30px">40 cm</div>
<div class="t dim center" style="left:526px;top:24px">10 cm</div>
<div class="t dim center" style="left:770px;top:30px">40 cm</div>
<div class="t dim center" style="left:1006px;top:24px">10 cm</div>
<div class="t dim dim-v" style="left:1078px;top:104px">10 cm</div>
<div class="t dim dim-v" style="left:1088px;top:440px">60 cm</div>
<div class="t dim dim-v" style="left:1078px;top:776px">10 cm</div>

<!-- front panel text -->
<section class="panel-front">
  <div class="t flap-label" style="left:287px;top:93px">Export Quality<b>52.5</b>CEMENT</div>
  <div class="t brand-front center" style="left:282px;top:174px">LARKFIELD</div>
  <div class="t brand-seal center" style="left:282px;top:306px">Larkfield</div>
  <div class="t front-cement center" style="left:284px;top:461px">CEMENT</div>
  <div class="t spec-title center" style="left:274px;top:569px">Portland Cement</div>
  <div class="t spec-std center" style="left:276px;top:596px">EN 197-1 (2000) , Strength Class 52.5</div>
  <div class="t export-line center" style="left:284px;top:637px">Export Quality</div>
  <div class="t export-line center" style="left:284px;top:665px">Product of Myanmar</div>
  <div class="t net-weight center" style="left:284px;top:696px">Net Weight&nbsp; 50 Kg</div>
</section>

<!-- gusset text -->
<div class="t gusset-seal" style="left:526px;top:230px">Larkfield</div>
<div class="t gusset-title" style="left:528px;top:500px">LARKFIELD<span>CEMENT</span></div>
<div class="t gusset-seal" style="left:1007px;top:230px">Larkfield</div>
<div class="t gusset-title" style="left:1008px;top:500px">LARKFIELD<span>CEMENT</span></div>

<!-- back panel text -->
<section class="panel-back">
  <div class="t brand-back" style="left:642px;top:172px">LARKFIELD<span>CEMENT</span></div>

  <div class="info-bar" style="top:228px">APPLICATIONS</div>
  <div class="t info-text" style="left:624px;top:252px">. Suitable for general concrete products.</div>

  <div class="info-bar" style="top:270px">MIXING INSTRUCTIONS</div>
  <div class="t mix-head" style="left:624px;top:294px">. Applications</div>
  <div class="t mix-head" style="left:727px;top:294px">Cement</div>
  <div class="t mix-head" style="left:774px;top:294px">Sand</div>
  <div class="t mix-head" style="left:810px;top:294px">Aggregate</div>
  <div class="t mix-head" style="left:862px;top:294px">Water</div>
  <div class="t mix-head" style="left:624px;top:323px">. Lean Concrete</div>
  <div class="t mix-head" style="left:624px;top:352px">. General Concrete</div>
  <div class="t mix-head" style="left:877px;top:350px">or</div>

  <div class="info-bar" style="top:373px">RECOMMENDATIONS</div>
  <div class="t info-small" style="left:624px;top:395px">. During 1-3 days of curing process, concrete should be sprayed with water to avoid crack.</div>
  <div class="t info-small" style="left:624px;top:413px">. A bag of cement should be finished within 1 day. If not, seal the bag tightly.</div>

  <div class="info-bar" style="top:428px">PRECAUTIONS</div>
  <div class="t info-small" style="left:670px;top:451px">Lift with care.</div>
  <div class="t info-small" style="left:670px;top:475px">Wear gloves while mixing or handling dry cement.</div>
  <div class="t info-small" style="left:670px;top:499px">Wear a mask while mixing dry cement.</div>
  <div class="t info-small" style="left:670px;top:522px">Keep cement away from child's reach.</div>
  <div class="t info-small" style="left:670px;top:544px;line-height:9px">Cement should be stored under shade and away from moisture<br>with pallets being raised above the ground.</div>

  <div class="t maker-intro" style="left:665px;top:579px">Manufactured and distributed by :</div>
  <div class="t maker-name" style="left:665px;top:596px">SILVERBAY CEMENT CO.,LTD.</div>
  <div class="t maker-address" style="left:665px;top:620px">
    No.48, 12<sup>th</sup> Street,<br>
    Between 20<sup>th</sup> and 21<sup>st</sup> Streets<br>
    Eastgate Township<br>
    Mandalay , Myanmar<br>
    Tel :&nbsp; (95)2 41205 , (95)2 41206 , (95)2 58317<br>
    <span class="indent">(95)2 41207 , (95)2 52904 , (95)2 63371</span><br>
    Fax : (95)2 49180 , Email : info@silverbaycement.com<br>
    www.silverbaycement.com
  </div>

  <div class="t grade-label center" style="left:768px;top:763px">Export Quality<b>52.5</b>CEMENT</div>
</section>

</main>
</body>
</html>
```